new roofing company card

New primary business card for roofing company.

Industry/Entity Type

Residential roofing/Specializing in Asphalt and Standing seam metal roofing

Contact Information for Business Card

Phone number is: 555 471 2086 Email: support@halvenshingleworks.example website: www.halvenshingleworks.example

Colors
EB3D1F
EC4F4E
F09395
F8D3D4
FCEDEE

```html
<!DOCTYPE html>
<html lang="en">
<head>
<meta charset="utf-8">
<title>Halven Shingleworks – Business Card</title>
<link rel="stylesheet" href="https://fonts.googleapis.com/css2?family=Cinzel:wght@400;600&family=Montserrat:wght@400;500;600&display=swap">
<style>
  :root {
    --page: #4a4a4a;
    --card: #232323;
    --red: #c8372b;
    --white: #f4f4f4;
    --muted: #4d4d4d;
    --serif: "Cinzel", "Times New Roman", serif;
    --sans: "Montserrat", Arial, sans-serif;
  }
  * { margin: 0; padding: 0; box-sizing: border-box; }
  html, body { width: 1200px; height: 875px; overflow: hidden; }
  body {
    background: var(--page);
    display: flex;
    flex-direction: column;
    align-items: center;
    justify-content: center;
    gap: 48px;
  }
  .card {
    position: relative;
    width: 560px;
    height: 320px;
    background: var(--card);
    border-radius: 20px;
    overflow: hidden;
  }

  /* Back */
  .card-back .wordmark {
    position: absolute;
    top: 82px;
    left: 0;
    right: 0;
    text-align: center;
    font-family: var(--serif);
    font-weight: 600;
    color: var(--muted);
    line-height: 1.05;
  }
  .wordmark .primary { display: block; font-size: 52px; letter-spacing: 2px; }
  .wordmark .secondary { display: block; font-size: 20px; letter-spacing: 5px; }
  .services {
    position: absolute;
    top: 212px;
    left: 150px;
    font-family: var(--sans);
    font-size: 15px;
    color: var(--white);
    line-height: 1.5;
  }
  .services h2 { font-size: 16px; font-weight: 500; color: var(--red); }
  .services ul { list-style: none; }
  .services li::before { content: "•"; color: var(--red); margin-right: 8px; }

  /* Front */
  .card-front .wordmark {
    position: absolute;
    top: 44px;
    left: 40px;
    font-family: var(--serif);
    font-weight: 600;
    color: var(--white);
    line-height: 1.05;
  }
  .card-front .wordmark .primary { font-size: 40px; }
  .card-front .wordmark .secondary { font-size: 15px; letter-spacing: 4px; }
  .feature-mark {
    position: absolute;
    top: 40px;
    right: 34px;
    font-family: var(--serif);
    font-weight: 600;
    font-size: 62px;
    color: var(--red);
    line-height: 1;
  }
  .person {
    position: absolute;
    top: 160px;
    left: 60px;
    padding-left: 18px;
  }
  .person::before {
    content: "";
    position: absolute;
    left: 0;
    top: 6px;
    width: 8px;
    height: 44px;
    background: var(--red);
    border-radius: 2px;
  }
  .person .name { font-family: var(--serif); font-weight: 400; font-size: 26px; color: var(--red); letter-spacing: 1px; }
  .person .title { font-family: var(--sans); font-size: 15px; color: var(--white); }
  .contact {
    position: absolute;
    top: 234px;
    left: 78px;
    list-style: none;
    font-family: var(--sans);
    font-size: 14px;
    color: var(--white);
    line-height: 1.6;
  }
  .contact li { display: flex; align-items: center; gap: 8px; }
  .contact svg { width: 12px; height: 12px; fill: var(--red); flex: none; }
</style>
</head>
<body>
  <section class="card card-back">
    <div class="wordmark">
      <span class="primary">HALVEN</span>
      <span class="secondary">SHINGLEWORKS</span>
    </div>
    <div class="services">
      <h2>Specializing in:</h2>
      <ul>
        <li>Asphalt shingle installation</li>
        <li>Standing seam metal installation</li>
      </ul>
    </div>
  </section>

  <section class="card card-front">
    <div class="wordmark">
      <span class="primary">HALVEN</span>
      <span class="secondary">SHINGLEWORKS</span>
    </div>
    <div class="feature-mark">HALVEN</div>
    <div class="person">
      <p class="name">DANIEL MARSH</p>
      <p class="title">President</p>
    </div>
    <ul class="contact">
      <li><svg viewBox="0 0 24 24"><path d="M6.6 10.8a15 15 0 0 0 6.6 6.6l2.2-2.2a1 1 0 0 1 1-.25 11.4 11.4 0 0 0 3.6.57 1 1 0 0 1 1 1V20a1 1 0 0 1-1 1A17 17 0 0 1 3 4a1 1 0 0 1 1-1h3.5a1 1 0 0 1 1 1c0 1.25.2 2.45.57 3.57a1 1 0 0 1-.25 1z"/></svg>555 471 2086</li>
      <li><svg viewBox="0 0 24 24"><path d="M2 5h20v14H2z M2 5l10 8 10-8" stroke="#232323" stroke-width="1.5"/></svg>support@halvenshingleworks.example</li>
      <li><svg viewBox="0 0 24 24"><circle cx="12" cy="12" r="10"/><path d="M2 12h20M12 2c3 3 3 17 0 20M12 2c-3 3-3 17 0 20" stroke="#232323" stroke-width="1.5" fill="none"/></svg>www.halvenshingleworks.example</li>
    </ul>
  </section>
</body>
</html>
```